1. Overview of company:
Copper Fern Mobile solutions private Ltd is one of the leading innovators & providers of Value added services (VAS) and telecom solutions to the top telecom operators across the world. We are the pioneer of several telecom technologies and products with our solutions empowering over 40 telecom giant in 51 countries.

2. Product Overview:
Vocal Twist is the most innovative voice morphing mobile app that has revolutionized the concept of IVR based offerings for telecom operators across the world. It lets you talk to your friend in a voice of your choice at just the press of a button. In addition to every call, users can now speak to their friends with background sounds of their choice.

In simple words: If person A calls person B, person A can choose the voice he wants B to listen, Words and sentences remain same just the voice changes. Person A can even activate a background sound for both of them while talking.

3. Objective of the design:
The purpose of this campaign is to establish Vocal Twist as Innovative, Lively, Youthful, Fun mobile app generally used for spreading smiles via pranks. The primary objective is to persuade the audience to download and use Vocal Twist mobile app, as well as to spread and characterize this new app.

4. Product layout:
Page 1: Landing Page
- pictorial explanation, what Vocal Twist stands for

Page 2: Home Screen options
-Navigation to vocal twist
-Navigation to sound scenery

Page 3: Vocal Twist options
-Female
-Cartoon
-King
-Bunny

Page 4: Sound scenery options
-Romantic
-Airport
-Traffic
-Football
-Church
-Beach

5. Target Audience
The users of the mobile app will be teenager whose age ranges from 16-27. The demographics are not restricted to a particular country and will be present on global level.

6. Deliverable
- 4 Uncoded screen and icon for mobile app "Vocal Twist"
- Our company name is "Copper Fern" , we would like to see designs that use Black and Green, at the same time its not mandatory.
-Design should communicate what the app stands for "Changing voice of caller"

Target Market(s)

User of the mobile app will be teenagers whose age ranges from 16-27. The demographics are not restricted to a particular country and will be present on global level. It's for masses.

Industry/Entity Type

Telecommunications

Requirements
Must have
• The design should be self explanatory, what the app stands for.
• Editable format for integration purpose.
Nice to have
• Would prefer Icons and very few words.
• Professional, elegant at the same time trendy designs.

```html
<!DOCTYPE html>
<html lang="en">
<head>
<meta charset="utf-8">
<title>Vocal Twist – Mobile UX/UI Apps design</title>
<link href="https://fonts.googleapis.com/css2?family=Roboto+Condensed:wght@300;400&display=swap" rel="stylesheet">
<style>
:root{
  --green:#5cbf4a;
  --green-deep:#46b04b;
  --green-bright:#7dc242;
  --lime:#8cc63f;
  --yellow:#d7df23;
  --ink:#111;
  --ring-dark:#1f3d1a;
  --ring-mid:#2d5a24;
  --city-top:#5d5d5d;
  --city-bottom:#2c2c2c;
  --white:#fff;
  --muted:#9a9a9a;
  --row-line:rgba(255,255,255,.35);
  --stage-top:#8f8f8f;
  --stage-bottom:#f2f2f2;
}
*{box-sizing:border-box;margin:0;padding:0}
html,body{width:1200px;height:900px;overflow:hidden}
body{position:relative;font-family:"Roboto Condensed",Arial,sans-serif;color:var(--white);
  background:linear-gradient(var(--stage-top),var(--stage-bottom) 85%)}
.banner{position:absolute;left:0;top:0;width:1200px;height:222px;
  background:linear-gradient(115deg,var(--green-bright),var(--green-deep))}
.brand{position:absolute;left:40px;top:86px;display:flex;align-items:center;gap:14px;
  font-size:42px;font-weight:400;letter-spacing:.5px}
.brand-dot{width:18px;height:18px;border:2px solid var(--white);border-radius:50%}
.tagline{position:absolute;right:38px;top:92px;font-size:28px;font-weight:300}
.footer-band{position:absolute;left:0;bottom:0;width:1200px;height:14px;background:var(--green)}

.screen{position:absolute;overflow:hidden;box-shadow:0 12px 28px rgba(0,0,0,.35)}
.city{position:absolute;inset:0;background:linear-gradient(var(--city-top),var(--city-bottom))}
.status{position:absolute;left:0;top:0;right:0;height:20px;display:flex;justify-content:space-between;
  align-items:center;padding:0 8px;font-size:8px;background:rgba(0,0,0,.35)}

/* list screens */
.list-screen{top:330px;width:190px;height:385px}
.drawer-edge{position:absolute;left:0;top:20px;width:20px;height:262px;background:var(--green)}
.drawer-line{position:absolute;left:20px;top:20px;width:1px;bottom:0;background:var(--white)}
.list-title{position:absolute;left:0;right:0;top:44px;text-align:center;color:var(--lime);font-size:15px}
.options{position:absolute;left:42px;right:0;top:76px;list-style:none}
.list-screen.right .options{left:0;right:40px}
.options li{height:40px;line-height:40px;text-align:center;font-size:14px;font-weight:300;
  color:#ddd;border-top:1px solid var(--row-line);position:relative}
.options li.selected{background:rgba(0,0,0,.7)}
.options .chev{position:absolute;right:10px;top:0;font-size:12px}
.back{position:absolute;left:50%;bottom:30px;width:44px;height:44px;margin-left:-22px;
  border:1.5px solid var(--white);border-radius:50%}

/* feature screens */
.feature{top:306px;width:226px;height:430px}
.tabs{position:absolute;top:20px;left:0;right:0;height:40px;background:#1b1b1b;display:flex;
  justify-content:space-between;align-items:center;padding:0 10px;font-size:12px}
.tabs .off{color:var(--muted);font-weight:300}
.tab-rail{position:absolute;left:0;right:0;bottom:0;height:3px;background:#333}
.tab-rail i{position:absolute;top:0;height:3px;width:50%;background:var(--white)}
.panel{position:absolute;top:60px;left:0;right:0;height:272px;
  background:linear-gradient(135deg,var(--lime),var(--green-deep))}
.panel-corner{position:absolute;left:0;top:0;width:0;height:0;border-top:36px solid #9ccf5a;border-right:36px solid transparent}
.hero{position:absolute;left:43px;top:10px}
.panel-label{position:absolute;left:0;right:0;top:236px;text-align:center;font-size:12px;color:var(--ink)}
.picker{position:absolute;left:32px;right:12px;top:358px;height:42px;border-radius:21px;background:#0d0d0d;
  display:flex;align-items:center;justify-content:space-between;padding:0 4px;font-size:15px;font-weight:300;color:#bbb}
.picker-btn{width:32px;height:32px;border-radius:50%;background:var(--lime);display:flex;align-items:center;justify-content:center}

/* landing */
.landing{left:456px;top:264px;width:288px;height:510px}
.landing-name{position:absolute;left:0;right:0;top:205px;text-align:center;font-size:30px}
.intro-band{position:absolute;left:0;right:0;top:372px;height:76px;background:rgba(92,191,74,.85);
  display:flex;align-items:center;justify-content:center;text-align:center;font-size:13px;font-weight:300;line-height:16px}
.intro-band::before{content:"";position:absolute;top:-8px;left:50%;margin-left:-8px;
  border-left:8px solid transparent;border-right:8px solid transparent;border-bottom:8px solid rgba(92,191,74,.85)}
.legal{position:absolute;left:0;right:0;bottom:20px;text-align:center;font-size:8px;color:#bbb;line-height:10px}
</style>
</head>
<body>
<header class="banner">
  <div class="brand"><span class="brand-dot"></span>vocal twist</div>
  <div class="tagline">Mobile UX/UI Apps design</div>
</header>

<!-- voice list -->
<section class="screen list-screen" style="left:20px">
  <div class="city" role="img" aria-label="Blurred black and white city skyline photo"></div>
  <div class="status"><span>●●●○○ Carrier</span><span>16:05</span><span>67%</span></div>
  <div class="drawer-edge"></div><div class="drawer-line"></div>
  <div class="list-title" style="left:42px">SELECT VOICE</div>
  <ul class="options">
    <li>Female</li><li>Cartoon</li><li>King</li><li class="selected">Bunny</li>
  </ul>
  <svg class="back" viewBox="0 0 44 44"><path d="M30 22H14M20 16l-6 6 6 6" fill="none" stroke="#fff" stroke-width="1.5"/></svg>
</section>

<!-- voice changer -->
<section class="screen feature" style="left:220px">
  <div class="city" role="img" aria-label="Blurred black and white city skyline photo"></div>
  <div class="status"><span>●●●○○ Carrier</span><span>16:05</span><span>67%</span></div>
  <div class="tabs"><span>Voice changer</span><span class="off">Background sound</span><div class="tab-rail"><i style="left:0"></i></div></div>
  <div class="panel">
    <div class="panel-corner"></div>
    <svg class="hero" width="140" height="150" viewBox="0 0 140 150">
      <circle cx="70" cy="75" r="70" fill="var(--ring-mid)"/>
      <path d="M8 100 A70 70 0 0 0 132 100" fill="none" stroke="var(--yellow)" stroke-width="4"/>
      <circle cx="70" cy="72" r="62" fill="var(--ring-dark)"/>
      <circle cx="70" cy="72" r="55" fill="none" stroke="#fff" stroke-width="3"/>
      <g fill="none" stroke="#fff" stroke-width="2.5" stroke-linecap="round">
        <rect x="61" y="42" width="18" height="34" rx="9"/>
        <path d="M53 66a17 17 0 0 0 34 0M70 83v14M60 97h20"/>
      </g>
    </svg>
    <div class="panel-label">Voice changer</div>
  </div>
  <div class="picker">
    <span class="picker-btn"><svg width="14" height="14"><circle cx="7" cy="7" r="5" fill="#1b1b1b"/></svg></span>
    <span>Bunny</span>
    <span class="picker-btn"><svg width="16" height="14"><path d="M2 3h12M2 7h12M2 11h12" stroke="#111" stroke-width="2"/></svg></span>
  </div>
</section>

<!-- landing -->
<section class="screen landing">
  <div class="city" role="img" aria-label="Blurred black and white city skyline photo"></div>
  <div class="status"><span>●●●○○ Carrier</span><span>16:05</span><span>67%</span></div>
  <div class="landing-name">vocal twist</div>
  <div class="intro-band">call &amp; change your contact voice<br>with background sound</div>
  <div class="legal">© 2015, Copper Fern Mobile solutions private Ltd.<br>All right reserved</div>
</section>

<!-- background sound -->
<section class="screen feature" style="left:754px">
  <div class="city" role="img" aria-label="Blurred black and white city skyline photo"></div>
  <div class="status"><span>●●●○○ Carrier</span><span>16:05</span><span>67%</span></div>
  <div class="tabs"><span>Voice changer</span><span class="off">Background sound</span><div class="tab-rail"><i style="left:50%"></i></div></div>
  <div class="panel">
    <div class="panel-corner"></div>
    <svg class="hero" width="140" height="150" viewBox="0 0 140 150">
      <circle cx="70" cy="75" r="70" fill="var(--ring-mid)"/>
      <path d="M8 100 A70 70 0 0 0 132 100" fill="none" stroke="var(--yellow)" stroke-width="4"/>
      <circle cx="70" cy="72" r="62" fill="var(--ring-dark)"/>
      <circle cx="70" cy="72" r="55" fill="none" stroke="#fff" stroke-width="3"/>
      <g fill="none" stroke="#fff" stroke-width="2.5">
        <circle cx="70" cy="72" r="22"/>
        <ellipse cx="70" cy="72" rx="10" ry="22"/>
        <path d="M48 72h44M52 61h36M52 83h36"/>
      </g>
    </svg>
    <div class="panel-label">Background sound</div>
  </div>
  <div class="picker">
    <span class="picker-btn"><svg width="16" height="16" viewBox="0 0 16 16"><path d="M8 1v14M2 9l6-3 6 3M5 15l3-1 3 1" stroke="#111" stroke-width="2" fill="none"/></svg></span>
    <span>Airport</span>
    <span class="picker-btn"><svg width="16" height="14"><path d="M2 3h12M2 7h12M2 11h12" stroke="#111" stroke-width="2"/></svg></span>
  </div>
</section>

<!-- sound list -->
<section class="screen list-screen right" style="left:990px">
  <div class="city" role="img" aria-label="Blurred black and white city skyline photo"></div>
  <div class="status"><span>●●●○○ Carrier</span><span>16:05</span><span>67%</span></div>
  <div class="list-title" style="right:40px">SELECT VOICE</div>
  <ul class="options">
    <li>Romantic<span class="chev">︿</span></li><li class="selected">Airport</li><li>Traffic</li><li>Football</li><li>Church<span class="chev">﹀</span></li>
  </ul>
  <svg class="back" style="margin-left:-42px" viewBox="0 0 44 44"><path d="M30 22H14M20 16l-6 6 6 6" fill="none" stroke="#fff" stroke-width="1.5"/></svg>
</section>

<div class="footer-band"></div>
</body>
</html>
```